Virtual Reality company needs business card design

We would like a business card that is simple and memorable. Vantelo is a global startup based in San Francisco and Singapore. We are a company with products and services for both the B2B and B2C audiences. We develop platforms with educational content, and allow people to interact with the content in a virtual environment setting. Our end user will be able to learn and 'see' the world's culture and history from the comfort of their home. The business card will primarily be used for B2B audience and not overly corporate in image, but requires a universal appeal - evoking sense of friendliness and innovation. Attached is our logo with two color options. We are open to single-sided or double-sided designs. EPS/AI files will be provided to winning designer at final design stage.

Other text that will be included in card: (Name), (Address), (Tel), (Email), (Website)

Include option of having TWO QR codes which are 0.5 inch x 0.5 inch each
Updates

Dear Designers,

Thank you for your submissions. We are currently in process of reviewing your designs and will make a decision in the next few days.

Regards,
Vantelo

Industry/Entity Type

Environment

Font styles to use
Serif
Sans Serif

Requirements
Must have
• Spacing for Name, Address, Tel, Email, Web address
Should not have
• Limit the number of colors utilised.

```html
<!DOCTYPE html>
<html lang="en">
<head>
<meta charset="utf-8">
<title>Vantelo Business Card</title>
<link href="https://fonts.googleapis.com/css2?family=Arimo:wght@400;700&display=swap" rel="stylesheet">
<style>
  :root {
    --backdrop: #d9dadc;
    --card-white: #f4f5f6;
    --sky-top: #80c6e8;
    --sky-bottom: #3a8ec6;
    --brand-blue: #3d94cc;
    --ink: #333537;
    --ink-soft: #4a4c4f;
    --charcoal: #3a3b3d;
    --ghost: #dcdcdd;
  }
  * { margin: 0; padding: 0; box-sizing: border-box; }
  html, body {
    width: 1200px; height: 800px; overflow: hidden;
    background: var(--backdrop);
    font-family: "Arimo", Arial, sans-serif;
  }
  .stage {
    position: relative; width: 1200px; height: 800px;
  }
  .card {
    position: absolute; top: 257px;
    width: 500px; height: 286px;
    overflow: hidden;
    box-shadow: 0 6px 18px rgba(0,0,0,0.18);
  }
  /* Back side */
  .card-back {
    left: 70px;
    background: linear-gradient(170deg, var(--sky-top), var(--sky-bottom));
  }
  .back-brand {
    position: absolute; left: 88px; top: 100px;
    display: flex; flex-direction: column; align-items: flex-end;
  }
  .back-web {
    font-size: 17px; color: var(--ink-soft); letter-spacing: 0.3px;
    margin-bottom: 2px; margin-right: 70px;
  }
  .back-wordmark {
    display: flex; align-items: center; gap: 14px;
  }
  .back-wordmark .name {
    font-size: 66px; font-weight: 400; color: #ffffff; letter-spacing: 1px; line-height: 1;
  }
  .back-wordmark .dot {
    width: 40px; height: 40px; border-radius: 50%; background: #ffffff;
  }
  /* Front side */
  .card-front {
    left: 630px;
    background: var(--card-white);
  }
  .ghost-mark {
    position: absolute; left: 300px; top: 30px;
    width: 180px; height: 180px; border-radius: 50%;
    background: var(--ghost); opacity: 0.7;
  }
  .identity {
    position: absolute; left: 40px; top: 104px;
  }
  .person-name {
    font-size: 23px; color: var(--ink); letter-spacing: 0.5px; line-height: 1;
  }
  .person-role {
    font-size: 15px; color: var(--ink); margin-top: 3px;
  }
  .front-wordmark {
    display: flex; align-items: center; gap: 10px; margin-top: 6px;
  }
  .front-wordmark .name {
    font-size: 44px; color: var(--brand-blue); line-height: 1; letter-spacing: 0.5px;
  }
  .front-wordmark .dot {
    width: 26px; height: 26px; border-radius: 50%; background: var(--brand-blue);
  }
  .divider {
    position: absolute; left: 240px; top: 78px;
    width: 2px; height: 130px; background: var(--brand-blue);
  }
  .contact {
    position: absolute; left: 272px; top: 84px;
    font-size: 14px; color: var(--ink-soft); line-height: 1.3;
  }
  .contact .gap { height: 12px; }
  .contact .label { color: var(--brand-blue); }
  .bands {
    position: absolute; left: 0; bottom: 0; width: 500px; height: 40px;
  }
</style>
</head>
<body>
<main class="stage">
  <section class="card card-back" aria-label="Card back">
    <div class="back-brand">
      <p class="back-web">yourwebaddress@com</p>
      <div class="back-wordmark">
        <span class="name">Vantelo</span>
        <span class="dot"></span>
      </div>
    </div>
  </section>

  <section class="card card-front" aria-label="Card front">
    <div class="ghost-mark"></div>
    <div class="identity">
      <p class="person-name">YOUR NAME</p>
      <p class="person-role">Company Position</p>
      <div class="front-wordmark">
        <span class="name">Vantelo</span>
        <span class="dot"></span>
      </div>
    </div>
    <div class="divider"></div>
    <address class="contact" style="font-style: normal;">
      <p>111 Your Street Address</p>
      <p>206 Town, CT 00000</p>
      <div class="gap"></div>
      <p><span class="label">E:</span> youremail@domain.com</p>
      <p><span class="label">P:</span> 111-222-444</p>
      <p><span class="label">F:</span> 111-222-333</p>
    </address>
    <svg class="bands" viewBox="0 0 500 40" preserveAspectRatio="none" aria-hidden="true">
      <polygon points="0,26 170,26 180,40 0,40" fill="var(--brand-blue)"/>
      <polygon points="170,26 500,4 500,40 180,40" fill="var(--charcoal)"/>
    </svg>
  </section>
</main>
</body>
</html>
```